Need a stunning looking Business Card Design for my Telecom Business, Wow FACTOR!

I deal with high level IT Directors , and Contractors.
I need to impress them with a sleek , professional and unique business card.
Im thinking options as far as rounded edges, plastic , or even metal card or die cut on a corner.
Whatever looks better and leave an unforgettable first impression.
im looking for the wow factor.
Front should have the basics info (attached on the picture of current business card)
i would like to add picture of myself somewhere
Back side
should have logo and maybe some pictures or past projects, you can download from my website ( www.lumvexholdings.com)

```html
<!DOCTYPE html>
<html lang="en">
<head>
<meta charset="utf-8">
<title>Lumvex Technologies – Business Card</title>
<link rel="stylesheet" href="https://fonts.googleapis.com/css2?family=Michroma&family=Open+Sans:wght@400;600&display=swap">
<style>
  :root {
    --stage: #3a3a3c;
    --paper: #ffffff;
    --ink: #111418;
    --navy: #0b2a63;
    --navy-deep: #082050;
    --cyan: #13b3e6;
    --orange: #f59a0c;
    --silver: #c9ccd2;
    --muted: #2a2f38;
  }
  * { box-sizing: border-box; margin: 0; padding: 0; }
  html, body { width: 1200px; height: 900px; overflow: hidden; }
  body {
    background: var(--stage);
    font-family: "Open Sans", Arial, sans-serif;
    position: relative;
  }
  .card {
    position: absolute;
    width: 540px;
    height: 309px;
    border-radius: 26px;
    overflow: hidden;
  }
  /* Front */
  .card-front { left: 40px; top: 296px; background: var(--paper); color: var(--ink); }
  .wordmark {
    position: absolute; right: 36px; top: 26px; text-align: right;
  }
  .wordmark-name {
    font-family: "Michroma", sans-serif; font-size: 44px; line-height: 1;
    letter-spacing: 1px; color: var(--ink);
  }
  .wordmark-sub {
    font-family: "Michroma", sans-serif; font-size: 13px; letter-spacing: 12px;
    margin-top: 8px; color: var(--ink);
  }
  .name-band {
    position: absolute; left: 0; top: 98px; width: 430px; height: 62px;
    background: linear-gradient(90deg, var(--navy-deep) 0%, var(--navy) 40%, var(--cyan) 100%);
    padding: 9px 0 0 32px; color: #fff;
  }
  .person-name { font-size: 21px; font-weight: 600; letter-spacing: .5px; }
  .person-role { font-size: 11px; letter-spacing: .6px; margin-top: 1px; }
  .band-dot {
    position: absolute; left: 414px; top: 112px; width: 34px; height: 34px;
    border-radius: 50%; background: var(--navy);
  }
  .contacts {
    position: absolute; left: 32px; top: 178px; list-style: none;
    font-size: 11.5px; line-height: 20px; color: var(--muted);
  }
  .contacts li { display: flex; align-items: center; gap: 7px; }
  .contacts svg { width: 10px; height: 10px; fill: #1f7fd1; flex: none; }
  .tagline {
    position: absolute; left: 280px; top: 184px; font-size: 12.5px;
    line-height: 18px; color: var(--muted);
  }
  .corner-block {
    position: absolute; right: 0; bottom: 0; width: 92px; height: 96px;
    background: var(--orange);
  }
  /* Back */
  .card-back {
    left: 620px; top: 296px;
    background: linear-gradient(160deg, #123a80 0%, var(--navy) 55%, var(--navy-deep) 100%);
  }
  .back-mark {
    position: absolute; left: 0; right: 0; top: 104px;
    display: flex; justify-content: center; align-items: center; gap: 14px;
    font-family: "Michroma", sans-serif; font-size: 28px; color: var(--silver);
    letter-spacing: 1px;
  }
  .back-mark-dot { width: 16px; height: 16px; border-radius: 50%; background: var(--silver); }
  .back-sub {
    position: absolute; left: 0; right: 0; top: 148px; text-align: center;
    font-family: "Michroma", sans-serif; font-size: 10px; letter-spacing: 9px; color: var(--silver);
  }
  .back-url {
    position: absolute; left: 40px; right: 40px; top: 196px;
    display: flex; align-items: center; gap: 12px;
    font-size: 11px; letter-spacing: 1px; color: var(--silver);
  }
  .back-url .rule { flex: 1; height: 1px; background: var(--silver); opacity: .7; }
</style>
</head>
<body>
  <section class="card card-front" aria-label="Business card front">
    <div class="wordmark">
      <div class="wordmark-name">LUMVEX</div>
      <div class="wordmark-sub">TECHNOLOGIES</div>
    </div>
    <div class="name-band">
      <div class="person-name">MARCO REYES</div>
      <div class="person-role">OPERATIONS MANAGER</div>
    </div>
    <div class="band-dot"></div>
    <ul class="contacts">
      <li><svg viewBox="0 0 10 10"><path d="M2 0h2l1 3-1.3 1a5 5 0 0 0 2.3 2.3L7 5l3 1v2a2 2 0 0 1-2 2A8 8 0 0 1 0 2a2 2 0 0 1 2-2z"/></svg>(305) 555-0142 Miami</li>
      <li><svg viewBox="0 0 10 10"><path d="M2 0h2l1 3-1.3 1a5 5 0 0 0 2.3 2.3L7 5l3 1v2a2 2 0 0 1-2 2A8 8 0 0 1 0 2a2 2 0 0 1 2-2z"/></svg>(954) 555-0187 Broward</li>
      <li><svg viewBox="0 0 10 10"><path d="M2 0h2l1 3-1.3 1a5 5 0 0 0 2.3 2.3L7 5l3 1v2a2 2 0 0 1-2 2A8 8 0 0 1 0 2a2 2 0 0 1 2-2z"/></svg>(561) 555-0163 Palm Beach</li>
      <li><svg viewBox="0 0 10 10"><path d="M0 1h10v8H0z M1 2l4 3 4-3" fill="none" stroke="#1f7fd1" stroke-width="1.2"/></svg>info@lumvexholdings.com</li>
      <li><svg viewBox="0 0 10 10"><circle cx="5" cy="5" r="4.4" fill="none" stroke="#1f7fd1" stroke-width="1.2"/><path d="M1 5h8M5 .6c-2 2.6-2 6.2 0 8.8M5 .6c2 2.6 2 6.2 0 8.8" fill="none" stroke="#1f7fd1" stroke-width=".9"/></svg>www.lumvexholdings.com</li>
    </ul>
    <p class="tagline">Low Voltage Contractor<br>Offices in Miami,<br>Broward and Palm Beach</p>
    <div class="corner-block"></div>
  </section>

  <section class="card card-back" aria-label="Business card back">
    <div class="back-mark"><span class="back-mark-dot"></span>LUMVEX</div>
    <div class="back-sub">TECHNOLOGIES</div>
    <div class="back-url"><span class="rule"></span>WWW.LUMVEXHOLDINGS.COM<span class="rule"></span></div>
  </section>
</body>
</html>
```